Ridgeway Ore Advisory Business Card

Ridgeway Ore Advisory is a company that provides consulting services to the Mining Industry.

Whilst Ridgeway Ore Advisory is an Australian based company its client base is the global mining industry.

The essence of Ridgeway Ore Advisory is its a can do organisation that can make a difference to its clients by providing quality assistance and form lasting relationships.
Updates

Target Market(s)

The global Mining Industry.

Industry/Entity Type

Mining

Font styles to use
Serif

Colors

Designer to choose colors to be used in the design.

Requirements
Nice to have
• My thinking is the card would look good in black given the logo.

I would like to see written on the back side of the card " Providing Metallurgical, Management and Corporate Services to the Mining Industry"

```html
<!DOCTYPE html>
<html lang="en">
<head>
<meta charset="utf-8">
<title>Ridgeway Ore Advisory – Business Card</title>
<link rel="stylesheet" href="https://fonts.googleapis.com/css2?family=Crimson+Pro:wght@700&family=Roboto+Slab:wght@300;400&family=Tinos&display=swap">
<style>
  :root {
    --ink: #000000;
    --paper: #ffffff;
    --ore-orange: #ff6600;
    --card-edge: #7a7a7a;
    --sheet-edge: #000000;
  }
  * { margin: 0; padding: 0; box-sizing: border-box; }
  html, body {
    width: 1200px;
    height: 900px;
    overflow: hidden;
    background: var(--paper);
  }
  .sheet {
    position: relative;
    width: 1200px;
    height: 900px;
    border: 2px solid var(--sheet-edge);
    background: var(--paper);
    overflow: hidden;
  }
  .side-label {
    position: absolute;
    left: 243px;
    font-family: "Tinos", "Times New Roman", serif;
    font-size: 31px;
    line-height: 1;
    color: var(--ink);
  }
  .side-label--front { top: -2px; }
  .side-label--back { top: 462px; }

  .card {
    position: absolute;
    left: 245px;
    width: 711px;
    height: 406px;
    border: 1px solid var(--card-edge);
    background: var(--paper);
    overflow: hidden;
  }
  .card--front { top: 29px; }
  .card--back { top: 493px; }

  .edge-stripes {
    position: absolute;
    left: 0;
    bottom: 0;
    width: 22px;
    display: flex;
    flex-direction: column;
  }
  .edge-stripes span { display: block; height: 57px; background: var(--ink); }
  .edge-stripes span.accent { background: var(--ore-orange); }

  .corner-badge {
    position: absolute;
    top: 0;
    right: 0;
    width: 234px;
    height: 156px;
  }
  .corner-badge svg { display: block; width: 100%; height: 100%; }
  .corner-name {
    position: absolute;
    top: 54px;
    right: 24px;
    width: 150px;
    text-align: center;
    font-family: "Crimson Pro", Georgia, serif;
    font-weight: 700;
    font-size: 19px;
    line-height: 1.05;
    letter-spacing: 1px;
    text-transform: uppercase;
    color: var(--ore-orange);
  }

  .company-name {
    position: absolute;
    left: 40px;
    top: 128px;
  }
  .company-name__main {
    display: block;
    font-family: "Crimson Pro", Georgia, serif;
    font-weight: 700;
    font-size: 74px;
    line-height: 0.95;
    color: var(--ore-orange);
  }
  .company-name__sub {
    display: block;
    margin-top: 2px;
    font-family: "Crimson Pro", Georgia, serif;
    font-weight: 700;
    font-size: 25px;
    letter-spacing: 2.2px;
    line-height: 1;
    text-transform: uppercase;
    color: var(--ink);
  }

  .contact {
    position: absolute;
    right: 37px;
    top: 255px;
    text-align: right;
    font-family: "Roboto Slab", Georgia, serif;
    font-weight: 300;
    font-size: 16.5px;
    line-height: 24.7px;
    color: var(--ink);
    list-style: none;
  }

  .services {
    position: absolute;
    left: 0;
    right: 0;
    top: 82px;
    text-align: center;
    font-family: "Roboto Slab", Georgia, serif;
    font-weight: 300;
    font-size: 24px;
    line-height: 33px;
    color: var(--ink);
  }
</style>
</head>
<body>
<main class="sheet">
  <p class="side-label side-label--front">Side 1</p>
  <section class="card card--front" aria-label="Business card front">
    <div class="corner-badge">
      <svg viewBox="0 0 234 156" aria-hidden="true">
        <polygon points="0,0 234,0 234,102 71,156" fill="var(--ink)"/>
      </svg>
      <p class="corner-name">Ridgeway<br>Ore Advisory</p>
    </div>

    <h1 class="company-name">
      <span class="company-name__main">Ridgeway</span>
      <span class="company-name__sub">Ore Advisory</span>
    </h1>

    <ul class="contact">
      <li>Address : xxxxxxxxx</li>
      <li>xxxxxxxxxxx xxxxxxx</li>
      <li>Tel : xxxxxx xxxxxxx</li>
      <li>Email : xxxxxxxxxx@xxxx.com</li>
      <li>Website : www.ssssssssssssssss.com</li>
    </ul>

    <div class="edge-stripes" aria-hidden="true">
      <span></span><span class="accent"></span><span></span>
    </div>
  </section>

  <p class="side-label side-label--back">Side 2</p>
  <section class="card card--back" aria-label="Business card back">
    <p class="services">Providing Metallurgical,<br>Management and<br>Corporate Services to the Mining Industry</p>
    <div class="edge-stripes" aria-hidden="true">
      <span></span><span class="accent"></span><span></span>
    </div>
  </section>
</main>
</body>
</html>
```